Nexor Turbo Business Card Design

This is a start up company that has state of the art patented technology for turbo chargers,that can be used on engines, gas or diesel, for any type of automotive,aviation,marine or industrial purpose.
This technology will provide longer life,lower maintenance and better performance and help produce lower emissions with any turbocharged engine.Red would be a predominate color and the design should communicate the latest technology,economy and
Environmental concern.
This product will initially be distributed in the U.S.A. But should move rapidly to global use.
Updates

Thank you for your design submissions, I have increased the budget for this job because my initial order was too low for the quality of work shown, plus I would Like to see some more options. I have a meeting this Sunday with my other partners and would anticipate being able to give you some feedback by the Beginning of next week. Regards.

Thank you for everyone's participation. The deadline is still open until 6/15 and my partners and I have a meeting Scheduled this weekend. At this time we have not ruled anyone out, But will be making a decision during the course of our meeting and wil Decide which direction we will be going in by the beginning of the week. Thanks again, regards, Dan Ferris.

Hello everybody, Sorry for the delay in communication, we have been very busy in putting the start up together. We are still not decided on the design of the business card and have a wide range to choose from. I would anticipated we shall have an answer within the next two weeks. Regards, Dan Ferris.

Target Market(s)

Manufacturers and wholesalers' of OEM and replacement turbochargers

Industry/Entity Type

Industrial

Contact Information for Business Card

We need a logo that should incorporate the " Nexor, a " possibly super imposed over a turbo charger with the fan blades of the turbocharger showing in the center of the "a" .
Name,title,phone number and email address only, no street/mailing address at this time.
The full name of the company is
" Nexor Turbo Technologies LLC "
For the initial card you can use my info.
Daniel Ferris
VP Sales & Marketing
dferris@nexorturbotechnologies.com
555 014 2876

Requirements
Must have
• The Nexor A, the outline of a turbo charger
Nice to have
• Something classy and simple and worldly (global)
Should not have
• No engines,cars,boats,planes

```html
<!DOCTYPE html>
<html lang="en">
<head>
<meta charset="UTF-8">
<title>Nexor Turbo Technologies LLC – Business Card</title>
<link rel="stylesheet" href="https://fonts.googleapis.com/css2?family=Oswald:wght@400;500;700&display=swap">
<style>
  :root {
    --backdrop: #f46c5a;
    --card-red: #e63a22;
    --ink-white: #ffffff;
    --ink-black: #1b1413;
    --rule: rgba(255, 255, 255, 0.85);
  }
  * { box-sizing: border-box; margin: 0; padding: 0; }
  html, body {
    width: 1200px;
    height: 900px;
    overflow: hidden;
    background: var(--backdrop);
  }
  .canvas {
    position: relative;
    width: 1200px;
    height: 900px;
  }
  .card {
    position: absolute;
    left: 140px;
    top: 185px;
    width: 920px;
    height: 530px;
    background: var(--card-red);
    border-radius: 24px;
    font-family: "Oswald", "Arial Narrow", sans-serif;
    text-transform: uppercase;
    color: var(--ink-white);
  }
  .brand-mark {
    position: absolute;
    left: 52px;
    top: 205px;
    display: flex;
    align-items: center;
    gap: 14px;
  }
  .brand-mark__dot {
    width: 46px;
    height: 46px;
    border-radius: 50%;
    background: var(--ink-white);
  }
  .brand-mark__name {
    font-weight: 700;
    font-size: 52px;
    line-height: 1;
    letter-spacing: 1px;
    color: var(--ink-white);
  }
  .company {
    position: absolute;
    left: 330px;
    top: 42px;
    font-weight: 700;
    font-size: 62px;
    line-height: 1.02;
    letter-spacing: 0.5px;
  }
  .company__line--light { color: var(--ink-white); }
  .company__line--dark { color: var(--ink-black); }
  .rule {
    position: absolute;
    height: 2px;
    background: var(--rule);
  }
  .rule--upper { left: 300px; right: 40px; top: 200px; }
  .rule--lower { left: 300px; right: 40px; top: 365px; }
  .person {
    position: absolute;
    left: 380px;
    top: 225px;
  }
  .person__name {
    font-weight: 700;
    font-size: 44px;
    line-height: 1.05;
    color: var(--ink-white);
  }
  .person__title {
    font-weight: 500;
    font-size: 24px;
    line-height: 1.3;
    letter-spacing: 0.5px;
    color: var(--ink-black);
  }
  .contact {
    position: absolute;
    top: 445px;
    display: flex;
    align-items: center;
    gap: 12px;
    font-weight: 400;
    font-size: 28px;
    line-height: 1;
    color: var(--ink-white);
  }
  .contact--phone { left: 60px; }
  .contact--email { right: 54px; text-transform: none; font-size: 26px; }
  .contact__icon { width: 26px; height: 26px; flex: none; }
</style>
</head>
<body>
<main class="canvas">
  <section class="card" aria-label="Business card front">
    <div class="brand-mark">
      <span class="brand-mark__dot"></span>
      <span class="brand-mark__name">Nexor</span>
    </div>

    <h1 class="company">
      <span class="company__line--light">Nexor Turbo</span><br>
      <span class="company__line--dark">Technologies LLC</span>
    </h1>

    <div class="rule rule--upper"></div>

    <div class="person">
      <p class="person__name">Daniel Ferris</p>
      <p class="person__title">VP Sales &amp; Marketing</p>
    </div>

    <div class="rule rule--lower"></div>

    <p class="contact contact--phone">
      <svg class="contact__icon" viewBox="0 0 26 26" aria-hidden="true">
        <circle cx="13" cy="13" r="13" fill="#ffffff"/>
        <path d="M9 7.5c.6-.4 1.3-.2 1.6.4l1 2c.3.6.1 1.2-.4 1.5l-.8.5c.5 1.4 1.6 2.7 3 3.4l.6-.7c.4-.5 1.1-.6 1.6-.2l1.8 1.2c.5.4.6 1.1.2 1.6l-.8 1c-.6.7-1.6.9-2.5.5-3.3-1.4-5.8-4.2-6.8-7.6-.3-.9 0-1.9.7-2.5z" fill="#e63a22"/>
      </svg>
      <span>555 014 2876</span>
    </p>

    <p class="contact contact--email">
      <svg class="contact__icon" viewBox="0 0 26 26" aria-hidden="true">
        <circle cx="13" cy="13" r="13" fill="#ffffff"/>
        <rect x="6.5" y="8.5" width="13" height="9" rx="1" fill="#e63a22"/>
        <path d="M6.8 9l6.2 5 6.2-5" fill="none" stroke="#ffffff" stroke-width="1.3"/>
      </svg>
      <span>dferris@nexorturbotechnologies.com</span>
    </p>
  </section>
</main>
</body>
</html>
```